Vesk in Spain

web design of search platform. Enclosed please find an excel sheet with the info, as well as a picture of a webdesign we like (plumhollow). Idea is to have a modern, inviting website with main colors white, red and dark grey (text). The logo (pold in spain) will be changed to vesk, but you can use this logo for now. Please also use the character enclosed. We can ask this designer to also design the pictograms for the other items, just use something from the net for the design and we'll have it changed afterwards. The texts are enclosed in the word doc enclosed. Thank you!

Target Market(s)

people looking for property in Spain

Industry/Entity Type

Real Estate

Number of Pages Required

1 page

Other font styles liked:
• a font that goes well with the logo

Colors
ec1f27

Requirements
Must have
• a lot of white
• clean but fun look

```html
<!DOCTYPE html>
<html lang="en">
<head>
<meta charset="utf-8">
<title>Vesk in Spain – Find your agent</title>
<link href="https://fonts.googleapis.com/css2?family=Noto+Sans:wght@400;700&display=swap" rel="stylesheet">
<style>
  :root {
    --red: #ec1f27;
    --text: #5f5f5f;
    --heading: #666666;
    --dark: #222222;
    --white: #ffffff;
    --shadow: 0 1px 4px rgba(0,0,0,0.18);
  }
  * { box-sizing: border-box; margin: 0; padding: 0; }
  html, body {
    width: 970px; height: 1200px; overflow: hidden;
    background: var(--white);
    font-family: "Noto Sans", Arial, sans-serif;
    color: var(--text);
  }
  .page { position: relative; width: 970px; height: 1200px; }
  .section-title {
    position: absolute; left: 0; width: 970px; text-align: center;
    font-size: 21px; font-weight: 700; color: var(--heading);
  }
  .intro {
    position: absolute; top: 66px; left: 0; width: 970px; text-align: center;
    font-size: 12.5px; line-height: 20.5px;
  }
  .property-list {
    position: absolute; top: 153px; left: 72px;
    display: flex; gap: 22px;
  }
  .property-photo {
    width: 190px; height: 108px; box-shadow: var(--shadow);
    background: linear-gradient(180deg, #9fa9cf 0%, #c9c3d9 28%, #e2ddd8 48%, #9a8f86 66%, #5c8ab0 80%, #4a6b3a 100%);
  }
  .steps { position: absolute; top: 376px; left: 36px; width: 900px; }
  .step { margin-bottom: 10px; }
  .step h3 { font-size: 16px; font-weight: 700; color: var(--red); line-height: 24px; }
  .step p { font-size: 12.2px; line-height: 20px; padding-left: 1px; }
  .benefits {
    position: absolute; top: 901px; left: 54px;
    display: flex; gap: 35px;
  }
  .benefit-card {
    position: relative; width: 188px; height: 266px;
    background: var(--white); box-shadow: var(--shadow);
    text-align: center; padding: 14px 12px 0;
  }
  .benefit-card h4 { font-size: 16px; font-weight: 700; color: var(--red); line-height: 24px; margin-bottom: 1px; }
  .benefit-card p { font-size: 12.2px; line-height: 20.2px; color: var(--dark); }
  .cta {
    position: absolute; left: 0; bottom: 0; width: 100%; height: 36px;
    background: var(--red); color: var(--white);
    font-size: 15.5px; font-weight: 700; line-height: 36px;
    text-decoration: none; display: block;
  }
</style>
</head>
<body>
<main class="page">
  <h2 class="section-title" style="top:22px">Featured properties for sale</h2>
  <p class="intro">
    In Spain, every agent has access to the same properties for sale.<br>
    Therefor, the most important first step is to find the real estate agent who is willing to do the most for you.<br>
    The agent of your choice will show you the best properties for sale in your area and guide you through the entire process
  </p>
  <div class="property-list">
    <div class="property-photo" role="img" aria-label="Terraced white apartment building with pool at dusk"></div>
    <div class="property-photo" role="img" aria-label="Terraced white apartment building with pool at dusk"></div>
    <div class="property-photo" role="img" aria-label="Terraced white apartment building with pool at dusk"></div>
    <div class="property-photo" role="img" aria-label="Terraced white apartment building with pool at dusk"></div>
  </div>

  <h2 class="section-title" style="top:325px">vesk in 6 steps</h2>
  <ol class="steps" style="list-style:none">
    <li class="step"><h3>1. Tell vesk what you are looking for</h3>
      <p>Answer a few short questions about your goals and preferences, and vesk will start filtering agents to find the best ones for you.</p></li>
    <li class="step"><h3>2. Review your top agent matches</h3>
      <p>In a matter of seconds, we'll present you with up to 5 top agent matches based on your needs. Our results are 100% free, data- driven and unbiased. Take a look at each agent's profile and select the agents you want to compete for you.</p></li>
    <li class="step"><h3>3. Receive proposals within 24 hours</h3>
      <p>Compare the different proposals for total savings, services and agent background information from top estate agents in your area. You’re about to make one of the largest financial decisions of your life - vesk helps you make a fully informed decision.</p></li>
    <li class="step"><h3>4. Select your agent</h3>
      <p>At no cost and no obligation for you, select the agent you feel best suits your needs. No personal information is shared with real estate agents until you have accepted the winning bid.</p></li>
    <li class="step"><h3>5. Agent contact</h3>
      <p>The agent of your choice will contact you and, if you hire him, guide you through the entire buying, selling or renting process.</p></li>
    <li class="step"><h3>6. Close the deal on your house!</h3>
      <p>Your top agent closes the deal for you at the best price possible. Your estate agent just saved you lots of time and money.</p></li>
  </ol>

  <h2 class="section-title" style="top:837px">Why thousands use vesk to find an agent</h2>
  <div class="benefits">
    <article class="benefit-card">
      <h4>Easy to use</h4>
      <p>Sign up and get started in just a few easy steps. No more calling around, you’ll receive up to 5 proposals from top real estate agents.</p>
      <a class="cta" href="#">Get started</a>
    </article>
    <article class="benefit-card">
      <h4>Get the best deal</h4>
      <p>Sit back while agents compete by offering you their best commission rates and services they will per-form if they win your listing.</p>
      <a class="cta" href="#">Get started</a>
    </article>
    <article class="benefit-card">
      <h4>You’re in control</h4>
      <p>There is no obligation when selecting an agent. If for any reason you do not feel satisfied with your selection, you will have the option of selecting another agent from the offers received.</p>
      <a class="cta" href="#">Get started</a>
    </article>
    <article class="benefit-card">
      <h4>No ‘stalking’ by agents</h4>
      <p>You remain anonymous until such time as you select the agent that best meets your needs for services and cost savings. Only the agent you select receives your contact information.</p>
      <a class="cta" href="#">Get started</a>
    </article>
  </div>
</main>
</body>
</html>
```